Memoir book cover design

Book cover design for a sailing memoir to be published in four formats (Paperback, Hard Cover, eBook & Audiobook). The title of the book is "Drifting Ela Varrow" which is the name of the sailboat. Although I have several pictures of the boat, they are all too low-resolution, so I would like to incorporate a generic image of a sailboat on the front cover. I have specific fonts (Moondance & Cherish) for the boat name in the title (see uploaded files), that match the way they appeared on the boat itself. I have also included a logo that we might be able to use.
- Cherish, Moondance

```html
<!DOCTYPE html>
<html lang="en">
<head>
<meta charset="utf-8">
<title>Drifting Ela Varrow — Book Cover Wrap</title>
<link rel="stylesheet" href="https://fonts.googleapis.com/css2?family=Dancing+Script:wght@400;500&display=swap">
<style>
  :root {
    --gold: #f6c27a;
    --white: #ffffff;
    --sky-back-top: #bfc7bd;
    --sky-back-mid: #efe0bd;
    --horizon: #d29a58;
    --sea-back-top: #e8bb78;
    --sea-back-bottom: #55646a;
    --sky-front-top: #37444c;
    --sky-front-mid: #8e9590;
    --horizon-front: #cdb48f;
    --sea-front-top: #b8a284;
    --sea-front-bottom: #3f4d53;
    --spine-top: #584838;
    --spine-mid: #b27b4b;
    --spine-bottom: #5f4e40;
    --image-sail: #c9b9a3;
    --image-sail-light: #ddd0bc;
    --image-hull: #e4ddd2;
    --image-reflection: #4e5a5e;
    --image-edge: rgba(255,255,255,0.35);
    --script: "Dancing Script", cursive;
  }
  * { margin: 0; padding: 0; box-sizing: border-box; }
  html, body { width: 1200px; height: 857px; overflow: hidden; background: #ffffff; }
  .cover-wrap { position: relative; width: 1200px; height: 857px; overflow: hidden; }

  .back-cover {
    position: absolute; left: 0; top: 0; width: 567px; height: 857px;
    background: linear-gradient(to bottom,
      var(--sky-back-top) 0%, var(--sky-back-mid) 40%, #e9c48d 56%,
      var(--horizon) 61%, var(--sea-back-top) 63%, #d8ad72 78%, var(--sea-back-bottom) 100%);
  }
  .barcode-area {
    position: absolute; left: 329px; top: 711px; width: 183px; height: 105px;
    background: var(--white);
  }

  .spine {
    position: absolute; left: 567px; top: 0; width: 66px; height: 857px;
    background: linear-gradient(to bottom, var(--spine-top) 0%, #8a6a4c 35%, var(--spine-mid) 55%, #9c7250 70%, var(--spine-bottom) 100%);
  }
  .spine-text {
    position: absolute; left: 50%; white-space: nowrap;
    font-family: var(--script); font-size: 21px; color: var(--white);
    transform-origin: left center; transform: rotate(90deg) translateY(-50%);
  }
  .spine-title { top: 193px; margin-left: 2px; }
  .spine-author { top: 509px; margin-left: 2px; }

  .front-cover {
    position: absolute; left: 633px; top: 0; width: 567px; height: 857px;
    background: linear-gradient(to bottom,
      var(--sky-front-top) 0%, #59646a 25%, var(--sky-front-mid) 48%, var(--horizon-front) 61%,
      var(--sea-front-top) 63%, #7b7f78 76%, var(--sea-front-bottom) 100%);
  }
  .sailboat-image {
    position: absolute; left: 125px; top: 95px; width: 385px; height: 762px;
    background: linear-gradient(to bottom,
      var(--image-sail-light) 0%, var(--image-sail) 55%,
      var(--image-hull) 57%, var(--image-hull) 62%,
      #7d8584 64%, var(--image-reflection) 100%);
    border: 1px solid var(--image-edge);
    border-bottom: none;
    opacity: 0.85;
  }
  .front-title {
    position: absolute; left: 60px; top: 112px;
    font-family: var(--script); font-weight: 500; line-height: 1;
    text-shadow: 2px 3px 5px rgba(0,0,0,0.35);
  }
  .front-title .title-line-1 { display: block; font-size: 104px; color: var(--gold); }
  .front-title .title-line-2 { display: block; font-size: 92px; color: var(--white); margin-top: 8px; }
  .front-author {
    position: absolute; left: 84px; top: 705px;
    font-family: var(--script); font-size: 78px; color: var(--gold);
    text-shadow: 2px 3px 5px rgba(0,0,0,0.3); white-space: nowrap;
  }
</style>
</head>
<body>
  <main class="cover-wrap">
    <section class="back-cover" role="img" aria-label="Calm sea at sunset with a golden horizon">
      <div class="barcode-area"></div>
    </section>

    <section class="spine">
      <p class="spine-text spine-title">Drifting Ela Varrow</p>
      <p class="spine-text spine-author">Colm Harrity</p>
    </section>

    <section class="front-cover">
      <div class="sailboat-image" role="img" aria-label="Photograph of a two-masted sailboat under full sail on still water at dusk, with its reflection below"></div>
      <h1 class="front-title">
        <span class="title-line-1">Drifting</span>
        <span class="title-line-2">Ela Varrow</span>
      </h1>
      <p class="front-author">Colm Harrity</p>
    </section>
  </main>
</body>
</html>
```